Seller Looking for a luxurious diverse ethnic look...stunning but not overly seductive

I need a web Design for a company based in NEW YORK CITY called Velvet Harbor LLC. Initially I will be selling clothing and accessories as well as electronics on Tradora and hope to branch out. I want the whole experience for my customers and people I will buy from when they deal with me to be confident that this will be a velvet harbor and luxurious transaction.
Updates

Project Deadline Extended Reason: As I keep getting these great designs I continue to get more ideas and feel more time will help get us there. Added Thursday, July 16, 2015

Target Market(s)

ages 20-60

Industry/Entity Type

Clothing

Number of Pages Required

1 page

Font styles to use
Script

Colors
b768aa

Requirements
Must have
• Sleek and Luxurious feel and modern. I would like the page to look startling stunning yet not overly seductive and to include ethnic diversity. I like the illusion not knowing what the sight is selling since I am not targeting one area.
Should not have
• Do not want it to look generic or traditional

```html
<!DOCTYPE html>
<html lang="en">
<head>
<meta charset="utf-8">
<title>Velvet Harbor LLC</title>
<link href="https://fonts.googleapis.com/css2?family=Open+Sans:wght@400;600;700&family=Roboto+Slab:wght@600&display=swap" rel="stylesheet">
<style>
:root{
  --plum:#b768aa;
  --plum-dark:#9c4f90;
  --ink:#333;
  --muted:#888;
  --line:#e2e2e2;
  --soft:#f2f2f2;
  --white:#fff;
  --footer:#3b3b3b;
  --footer-base:#2f2f2f;
}
*{box-sizing:border-box;margin:0;padding:0}
html,body{width:1200px;height:2992px;overflow:hidden}
body{font-family:"Open Sans",Arial,sans-serif;color:var(--ink);background:var(--white);font-size:14px}
a{color:inherit;text-decoration:none}

.topbar{height:40px;background:var(--plum);color:var(--white);display:flex;align-items:center;justify-content:space-between;padding:0 56px;font-size:13px}
.topbar .call{font-weight:600;display:flex;align-items:center;gap:8px}
.topbar .call strong{font-size:16px}
.topbar .account{display:flex;gap:34px}
.topbar .account span{display:flex;align-items:center;gap:6px}

.header{height:112px;display:flex;align-items:center;justify-content:space-between;padding:0 56px}
.brand{font-family:"Roboto Slab",Georgia,serif;font-weight:600;font-size:22px;color:var(--plum);letter-spacing:1px}
.nav{display:flex;gap:6px}
.nav a{padding:8px 12px;font-size:14px;color:#555;border:1px solid transparent}
.nav a.active{border-color:var(--plum);color:var(--plum)}

.hero{position:relative;height:616px;background:linear-gradient(100deg,#7a7a7a 0%,#9a9a98 45%,#b3b2ae 100%)}
.hero .photo{position:absolute;left:140px;top:0;width:380px;height:616px;background:linear-gradient(180deg,#4a4a52 0%,#c8424f 60%,#8d2a35 100%);opacity:.55}
.hero .caption{position:absolute;left:640px;top:200px;color:var(--white);width:440px}
.hero h1{font-size:56px;font-weight:600;margin-bottom:18px}
.hero p{font-size:18px;line-height:1.45;margin-bottom:26px}
.btn{display:inline-block;background:var(--plum);color:var(--white);font-size:12px;font-weight:700;padding:9px 22px;letter-spacing:1px}
.hero .arrow{position:absolute;top:290px;width:36px;height:36px;background:var(--white);display:flex;align-items:center;justify-content:center}
.hero .arrow.left{left:0}.hero .arrow.right{right:0}
.dots{position:absolute;bottom:26px;left:0;right:0;display:flex;justify-content:center;gap:10px}
.dots span{width:12px;height:12px;border-radius:50%;border:2px solid var(--white)}
.dots span.on{background:var(--white)}

.promos{display:flex;gap:16px;padding:44px 56px;height:284px}
.promo{position:relative;flex:1;height:240px;padding:40px 24px}
.promo.women{background:linear-gradient(90deg,#f3c9b8,#e8d5cc)}
.promo.sale{background:linear-gradient(90deg,#f6f6f6,#ececec)}
.promo.tech{background:linear-gradient(180deg,#dcdcdc,#c5c5c5)}
.promo .shoe{position:absolute;left:40px;top:40px;width:150px;height:150px;background:radial-gradient(circle,#c0179b 0%,#d65fc0 50%,transparent 72%)}
.promo h3{font-size:24px;font-weight:700;color:var(--white);line-height:1.1;margin-bottom:14px}
.promo .link{font-size:12px;font-weight:700;color:var(--ink);border-bottom:2px solid var(--plum)}
.promo.women .link{color:var(--white)}
.promo.sale .offer{position:absolute;right:40px;top:54px;text-align:center;color:#444;font-size:30px;line-height:1.15}
.promo.sale .offer b{display:block;font-size:56px;color:var(--plum)}
.promo.sale .link{position:absolute;right:40px;bottom:26px}
.promo.tech .label{position:absolute;left:24px;bottom:24px}
.promo.tech h3{font-size:20px;margin-bottom:8px}

.products{background:var(--soft);padding:44px 68px 48px}
.products.featured{height:580px}
.products.latest{height:468px}
.section-title{text-align:center;color:var(--plum);font-size:16px;font-weight:700;letter-spacing:.5px;margin-bottom:30px}
.tabs{display:flex;justify-content:center;gap:10px;margin-bottom:36px}
.tabs span{background:var(--white);border:1px solid var(--line);font-size:12px;padding:5px 12px}
.tabs span.on{color:var(--plum)}
.grid{display:flex;gap:16px;justify-content:center}
.card{position:relative;width:252px;background:var(--white);text-align:center;padding-bottom:18px}
.card .img{height:200px;margin:0 auto}
.card .tag{position:absolute;right:-6px;top:10px;background:var(--plum);color:var(--white);font-size:11px;font-weight:700;padding:3px 12px}
.card h4{font-size:14px;font-weight:600;margin:12px 0 6px}
.price{font-size:13px}
.price s{color:var(--muted);margin-right:8px}
.price b{color:var(--plum)}
.view-all{display:block;width:176px;margin:50px auto 0;text-align:center;border:1px solid var(--plum);color:var(--plum);font-size:12px;font-weight:600;padding:9px 0;background:var(--white)}
.latest .view-all{margin-top:48px}
.latest .card .img{height:160px}

.banners{display:flex;gap:32px;padding:68px 56px 52px;height:336px}
.banner{position:relative;flex:1;height:216px}
.banner.electronics{background:linear-gradient(90deg,#2d3e5c,#5b86b8 55%,#98b7d8)}
.banner.collection{background:linear-gradient(90deg,#6c7075,#3e3a38 60%,#b24a3a)}
.banner .copy{position:absolute;color:var(--white)}
.banner.electronics .copy{left:260px;top:62px}
.banner.collection .copy{left:40px;top:66px}
.banner h3{font-size:30px;font-weight:700;line-height:1}
.banner small{display:block;font-size:13px;font-weight:600;margin:6px 0}
.banner .pct{font-size:22px;font-weight:700}
.banner .btn{padding:5px 14px;font-size:11px;margin-top:8px}

.features{display:flex;padding:52px 56px;height:212px;border-bottom:1px solid var(--line)}
.feature{flex:1;text-align:center;border-right:1px solid var(--line)}
.feature:last-child{border-right:0}
.feature svg{margin-bottom:10px}
.feature h5{font-size:13px;font-weight:700;margin-bottom:6px}
.feature p{font-size:12px;color:var(--muted)}

.footer{background:var(--footer);color:#ddd;height:260px;padding:40px 56px 0;display:flex;gap:60px}
.footer h6{color:var(--white);font-size:13px;font-weight:700;margin-bottom:18px}
.footer .col{flex:1;font-size:12px;line-height:1.9}
.newsletter form{display:flex;margin-top:12px}
.newsletter .field{flex:1;height:40px;border:1px solid #666;background:#444;color:#aaa;padding:10px 12px;font-size:12px}
.newsletter .go{width:44px;height:40px;background:var(--plum);display:flex;align-items:center;justify-content:center}
.social{display:flex;gap:8px;margin-bottom:28px}
.social span{width:34px;height:34px;background:var(--plum)}
.market{font-size:34px;font-weight:700;color:var(--white)}
.bottom{background:var(--footer-base);color:#aaa;height:32px;display:flex;align-items:center;justify-content:space-between;padding:0 56px;font-size:11px}
.bottom nav{display:flex;gap:22px}
</style>
</head>
<body>

<div class="topbar">
  <div class="call">
    <svg width="14" height="14" viewBox="0 0 24 24"><path fill="#fff" d="M6.6 10.8a15 15 0 0 0 6.6 6.6l2.2-2.2a1 1 0 0 1 1-.25 11.4 11.4 0 0 0 3.6.6 1 1 0 0 1 1 1V20a1 1 0 0 1-1 1A17 17 0 0 1 3 4a1 1 0 0 1 1-1h3.5a1 1 0 0 1 1 1c0 1.25.2 2.45.6 3.6a1 1 0 0 1-.25 1z"/></svg>
    Call Us: <strong>212.555.0148</strong>
  </div>
  <div class="account"><span>Login</span><span>My Cart</span><span>Checkout</span></div>
</div>

<header class="header">
  <div class="brand">VELVET HARBOR LLC</div>
  <nav class="nav">
    <a class="active">Home</a><a>About Us</a><a>Clothing</a><a>Accessories</a><a>Electronics</a><a>Blog</a><a>Contact Us</a>
  </nav>
</header>

<section class="hero">
  <div class="photo" role="img" aria-label="Fashion photo of a couple in stylish outfits against a concrete wall"></div>
  <div class="caption">
    <h1>Clothing</h1>
    <p>There are many variations of passages of Lorem Ipsum available, but the majority</p>
    <a class="btn">SHOP NOW &#8250;</a>
  </div>
  <div class="arrow left"><svg width="12" height="12" viewBox="0 0 12 12"><path d="M8 1 3 6l5 5" stroke="#555" stroke-width="2" fill="none"/></svg></div>
  <div class="arrow right"><svg width="12" height="12" viewBox="0 0 12 12"><path d="M4 1l5 5-5 5" stroke="#555" stroke-width="2" fill="none"/></svg></div>
  <div class="dots"><span></span><span class="on"></span><span></span><span></span><span></span></div>
</section>

<section class="promos">
  <div class="promo women" role="img" aria-label="Woman in a white outfit promoting women's clothing">
    <h3>WOMEN<br>CLOTHING</h3><span class="link">SHOP NOW</span>
  </div>
  <div class="promo sale">
    <div class="shoe" role="img" aria-label="Pink high-heel shoe"></div>
    <div class="offer">UPTO<b>45%</b>OFF!</div>
    <span class="link">SHOP NOW</span>
  </div>
  <div class="promo tech" role="img" aria-label="Living room with a wall-mounted television">
    <div class="label"><h3>ELECTRONICS</h3><span class="link">SHOP NOW</span></div>
  </div>
</section>

<section class="products featured">
  <h2 class="section-title">FEATURED PRODUCTS</h2>
  <div class="tabs"><span class="on">All</span><span>Clothing</span><span>Accessories</span><span>Electronics</span></div>
  <div class="grid">
    <div class="card"><span class="tag">NEW</span><div class="img" role="img" aria-label="Woman in a red dress" style="width:120px;background:linear-gradient(180deg,#f4e9e6,#c8202e 40%,#a3161f)"></div><h4>Clothing 1</h4><p class="price"><s>$60.00</s><b>$45.00</b></p></div>
    <div class="card"><span class="tag">NEW</span><div class="img" role="img" aria-label="Woman in a pink dress" style="width:120px;background:linear-gradient(180deg,#f3e7ea,#d66ba2 45%,#b84e86)"></div><h4>Clothing 2</h4><p class="price"><s>$60.00</s><b>$45.00</b></p></div>
    <div class="card"><span class="tag">NEW</span><div class="img" role="img" aria-label="Black digital camera" style="width:170px;background:radial-gradient(ellipse at center,#2a2a2a 35%,#fff 72%)"></div><h4>Camera</h4><p class="price"><s>$60.00</s><b>$45.00</b></p></div>
    <div class="card"><span class="tag">NEW</span><div class="img" role="img" aria-label="Man in a red checked shirt" style="width:120px;background:linear-gradient(180deg,#f2ece6,#c9463f 40%,#4a4f66 80%)"></div><h4>Men Shirt</h4><p class="price"><s>$60.00</s><b>$45.00</b></p></div>
  </div>
  <a class="view-all">VIEW ALL PRODUCTS &#8250;</a>
</section>

<section class="banners">
  <div class="banner electronics" role="img" aria-label="Hand holding a remote in front of a television">
    <div class="copy"><h3>SALE</h3><small>ON ALL ELECTRONICS</small><span class="pct">10%</span><br><a class="btn">SHOP NOW</a></div>
  </div>
  <div class="banner collection" role="img" aria-label="Man in a striped sweater and cap">
    <div class="copy"><h3>NEW COLLECTION</h3><small>THERE ARE MANY VARIATIONS</small><a class="btn">SHOP NOW</a></div>
  </div>
</section>

<section class="products latest">
  <h2 class="section-title">LATEST PRODUCTS</h2>
  <div class="grid">
    <div class="card"><div class="img" role="img" aria-label="Black headphones" style="width:160px;background:radial-gradient(circle,#333 30%,#fff 70%)"></div><h4>Headphone</h4><p class="price"><s>$60.00</s><b>$45.00</b></p></div>
    <div class="card"><div class="img" role="img" aria-label="Black leather men's shoes" style="width:160px;background:radial-gradient(ellipse,#1e1e1e 30%,#fff 70%)"></div><h4>Men Shoe</h4><p class="price"><s>$60.00</s><b>$45.00</b></p></div>
    <div class="card"><div class="img" role="img" aria-label="Smart watch with blue screen" style="width:140px;background:radial-gradient(circle,#2f6fb0 18%,#222 38%,#fff 68%)"></div><h4>Electronic Watch</h4><p class="price"><s>$60.00</s><b>$45.00</b></p></div>
    <div class="card"><div class="img" role="img" aria-label="Man in an orange t-shirt" style="width:120px;background:linear-gradient(180deg,#f3eee8,#e58a2e 45%,#3a5a8a 85%)"></div><h4>Men T Shirt</h4><p class="price"><s>$60.00</s><b>$45.00</b></p></div>
  </div>
  <a class="view-all">VIEW ALL PRODUCTS &#8250;</a>
</section>

<section class="features">
  <div class="feature">
    <svg width="26" height="22" viewBox="0 0 26 22"><path fill="#444" d="M1 3h15v11H1zM16 7h5l4 4v3h-9z"/><circle cx="6" cy="17" r="3" fill="#444"/><circle cx="20" cy="17" r="3" fill="#444"/></svg>
    <h5>FREE SHIPPING</h5><p>It is a long established</p>
  </div>
  <div class="feature">
    <svg width="24" height="22" viewBox="0 0 24 22"><path d="M3 13V11a9 9 0 0 1 18 0v2" stroke="#444" stroke-width="2.4" fill="none"/><rect x="1" y="12" width="5" height="8" rx="1" fill="#444"/><rect x="18" y="12" width="5" height="8" rx="1" fill="#444"/></svg>
    <h5>24X7 CUSTOMER SUPPORT</h5><p>It is a long established</p>
  </div>
  <div class="feature">
    <svg width="24" height="22" viewBox="0 0 24 22"><rect x="1" y="6" width="22" height="14" rx="2" fill="#444"/><path d="M8 6V3h8v3" stroke="#444" stroke-width="2.4" fill="none"/></svg>
    <h5>OUR SERVICES</h5><p>It is a long established</p>
  </div>
  <div class="feature">
    <svg width="24" height="22" viewBox="0 0 24 22"><rect x="1" y="3" width="22" height="16" rx="1" fill="#444"/><path d="M2 4l10 8 10-8" stroke="#fff" stroke-width="1.8" fill="none"/></svg>
    <h5>E-MAIL</h5><p>info@velvetharbor.com</p>
  </div>
</section>

<footer class="footer">
  <div class="col">
    <h6>CONTACT US</h6>
    <p>400 Mercer Street, Suite 12, New York, NY 10012</p>
    <p>212.555.0148 &nbsp;|&nbsp; info@velvetharbor.com</p>
  </div>
  <div class="col newsletter">
    <h6>NEWSLETTER SUBSCRIBE</h6>
    <p>Signup today and get updates</p>
    <form><span class="field">Enter Your Email Id</span><span class="go"><svg width="18" height="14" viewBox="0 0 18 14"><rect x="1" y="1" width="16" height="12" fill="none" stroke="#fff" stroke-width="1.6"/><path d="M1 1l8 6 8-6" stroke="#fff" stroke-width="1.6" fill="none"/></svg></span></form>
  </div>
  <div class="col">
    <h6>CONNECT WITH US</h6>
    <div class="social"><span></span><span></span><span></span><span></span></div>
    <div class="market">Tradora</div>
  </div>
</footer>
<div class="bottom">
  <nav><a>Home</a><a>About Us</a><a>Clothing</a><a>Accessories</a><a>Electronics</a><a>Blog</a><a>Contact Us</a></nav>
  <span>Copyright &copy; 2015 Velvet Harbor LLC. All Rights Reserved.</span>
</div>

</body>
</html>
```